Badgerline Custom Woodcraft Website design

Need a small website to showcase my products and take orders

would also like payment options

We do custom wood work along with cnc work in wood plastic and soft metals

we are based in edmonton alberta canada
Updates

Industry/Entity Type

Work

Number of Pages Required

3 page

Requirements
Nice to have
• Interview for for a woodworking magazine
• http://timberquarterlyexample.com/issue-1-02-august-2016/member-spotlight
• I would also like to see metal working/branding iron info
• Also adding the picture of me from the above interview is a nice touch

```html
<!DOCTYPE html>
<html lang="en">
<head>
<meta charset="utf-8">
<title>Badgerline Custom Woodcraft</title>
<link href="https://fonts.googleapis.com/css2?family=Roboto:wght@400;500;700&family=Ubuntu:ital,wght@0,400;0,500;0,700;1,400;1,500&family=Open+Sans:wght@400;600;700&display=swap" rel="stylesheet">
<style>
:root{
  --ink:#2b2118;
  --brown:#5a3a1e;
  --wood:#c98a4e;
  --wood-light:#e3b27a;
  --wood-dark:#8a5428;
  --orange:#d9772e;
  --orange-dark:#b25a1d;
  --red:#e01b1b;
  --blue:#1b4f9c;
  --navy:#1c2b5c;
  --nav:#2a2826;
  --footer:#17110c;
  --card-line:#d9b48a;
  --star:#f2a20c;
  --white:#ffffff;
  --muted:#444;
}
*{box-sizing:border-box;margin:0;padding:0}
html,body{width:1200px;height:2786px;overflow:hidden}
body{position:relative;background:var(--white);font-family:"Open Sans",Arial,sans-serif;color:var(--ink)}
.abs{position:absolute}

/* header */
.brand{left:52px;top:22px;height:52px;display:flex;align-items:center;gap:14px}
.brand-mark{width:52px;height:52px;border-radius:50%;background:var(--brown);flex:none}
.brand-name{font-family:"Ubuntu",sans-serif;font-weight:700;font-size:25px;color:var(--brown);line-height:1;white-space:nowrap}
.call-label{right:52px;top:8px;font-family:"Roboto",sans-serif;font-weight:700;font-size:15px;color:var(--blue);letter-spacing:.5px}
.phone{right:52px;top:22px;display:flex;align-items:center;gap:16px;font-family:"Roboto",sans-serif;font-weight:700;font-size:42px;line-height:52px;color:var(--blue)}
.hours{right:52px;top:77px;font-family:"Roboto",sans-serif;font-weight:700;font-size:12px;color:var(--ink)}

/* nav */
.navbar{left:0;top:97px;width:1200px;height:37px;background:var(--nav)}
.picker{top:5px;height:27px;background:#111;color:var(--white);font:700 12px "Roboto",sans-serif;display:flex;align-items:center;justify-content:space-between;padding:0 10px}
.picker.type{left:115px;width:225px}
.picker.qty{left:345px;width:67px}
.nav-links{left:480px;top:0;height:37px;display:flex;align-items:center;list-style:none}
.nav-links li{font:700 13px "Roboto",sans-serif;color:var(--white);text-align:center}

/* hero */
.hero{left:0;top:134px;width:1200px;height:423px;background:linear-gradient(90deg,#b06a32,#c98450 25%,#a9652f 50%,#c4814b 75%,#a86330)}
.hero-banner{left:0;top:214px;width:525px;height:232px;background:rgba(35,22,12,.88);clip-path:polygon(0 0,100% 0,72% 100%,0 100%)}
.hero-title{left:50px;top:225px;font:500 33px "Roboto",sans-serif;color:var(--white)}
.hero-tag{left:69px;top:279px;width:312px;height:70px;background:#0d0a08;color:var(--white);font:500 21px "Roboto",sans-serif;letter-spacing:2px;padding:10px 0 0 54px;line-height:1.25}
.hero-cta{left:0;top:362px;width:405px;height:38px;background:var(--red);color:var(--white);font:500 26px "Roboto",sans-serif;letter-spacing:-.5px;padding:2px 0 0 72px;clip-path:polygon(0 0,100% 0,94% 100%,0 100%)}
.hero-dots{left:148px;top:405px;display:flex;gap:10px}
.hero-dots span{width:12px;height:12px;border-radius:50%;border:2px solid #bbb;background:#555}
.hero-dots span:first-child{background:#eee}
.disc{border-radius:50%;border:3px solid rgba(255,255,255,.35)}

/* quote form */
.quote{left:895px;top:158px;width:245px;height:343px;background:#3a2516;border-radius:3px;box-shadow:0 4px 10px rgba(0,0,0,.4)}
.quote-head{left:10px;top:6px;width:225px;height:38px;background:linear-gradient(#e8c48e,#c9955a);color:var(--white);font:700 14px "Roboto",sans-serif;text-align:center;line-height:38px;letter-spacing:.5px}
.field{left:15px;width:215px;height:38px;background:var(--white);border-radius:2px;font:12px "Open Sans",sans-serif;color:#555;padding:11px 12px;display:flex;justify-content:space-between}
.submit{left:15px;top:301px;width:215px;height:34px;background:var(--orange);color:var(--white);font:700 12px "Roboto",sans-serif;text-align:center;line-height:34px;border-radius:2px}

/* welcome board */
.board{background:linear-gradient(180deg,#e5b27a,#cf9357 55%,#d8a06a);border:1px solid #b37a43;box-shadow:0 3px 6px rgba(0,0,0,.25)}
.welcome{left:87px;top:533px;width:1027px;height:136px}
.welcome h2{position:absolute;left:0;top:8px;width:100%;text-align:center;font:700 25px "Ubuntu",sans-serif;color:#5b3b1f}
.welcome p{position:absolute;left:80px;top:48px;width:870px;font:700 13.5px/1.55 "Ubuntu",sans-serif;color:var(--white)}
.welcome-tip{left:588px;top:668px;width:0;height:0;border-left:12px solid transparent;border-right:12px solid transparent;border-top:10px solid #c98c52}

/* designs */
.pill{left:344px;top:780px;width:512px;height:38px;border-radius:19px;background:linear-gradient(#e3ad72,#c98346);border:2px solid #b06d32;text-align:center;font:700 22px/34px "Ubuntu",sans-serif;color:#6b4421}
.row-label{left:110px;font:700 15px "Open Sans",sans-serif;color:var(--ink)}
.arrow-btn{width:34px;height:34px;border-radius:50%;border:2px solid var(--wood);background:var(--white)}
.card{width:198px;height:328px;border:1px solid var(--card-line);border-radius:4px;background:var(--white)}
.card-photo{position:absolute;left:6px;top:6px;width:184px;height:171px}
.card-title{position:absolute;left:0;top:190px;width:100%;text-align:center;font:700 11px "Open Sans",sans-serif}
.card-desc{position:absolute;left:14px;top:209px;width:170px;text-align:center;font:11px/1.45 "Open Sans",sans-serif;color:var(--muted)}
.card-rate{position:absolute;left:0;top:245px;width:100%;display:flex;justify-content:center;align-items:center;gap:10px}
.badge-new{position:absolute;left:10px;top:0;font:600 9px "Open Sans",sans-serif;color:var(--orange-dark);border:1px solid var(--orange);border-radius:9px;padding:1px 6px}
.stars{color:var(--star);font-size:15px;letter-spacing:1px}
.card-btn{position:absolute;left:32px;top:276px;width:132px;height:38px;background:linear-gradient(#e1934d,#c26c28);border-bottom:3px solid #8f4d18;color:var(--white);font:700 11px/35px "Open Sans",sans-serif;text-align:center;border-radius:2px}

/* recent */
.tile{position:absolute}
.tile-more{background:#2b4496;color:var(--white);font:700 15px/1.35 "Open Sans",sans-serif;text-align:center;padding-top:48px}

/* featured */
.navy-band{left:0;top:2266px;width:1200px;height:237px;background:linear-gradient(180deg,#1b2a5a,#22346a)}
.feature{left:158px;top:2203px;width:919px;height:122px}
.feature h3{position:absolute;left:44px;top:16px;font:400 30px "Ubuntu",sans-serif;color:var(--white)}
.feature .lede{position:absolute;left:44px;top:60px;font:700 16px "Ubuntu",sans-serif;color:#3a2413}
.feature .date{position:absolute;left:380px;top:98px;font:600 9.5px "Open Sans",sans-serif;color:#3a2413}
.portrait-frame{left:818px;top:2130px;width:200px;height:148px;background:var(--white);padding:7px;transform:rotate(-3deg);box-shadow:0 3px 8px rgba(0,0,0,.35)}
.caption{left:846px;top:2296px;font:italic 500 14px "Ubuntu",sans-serif;color:var(--white)}
.quote-text{left:88px;top:2358px;width:1030px;font:400 20px/1.4 "Open Sans",sans-serif;color:var(--white)}
.quote-name{left:88px;top:2430px;font:13px "Open Sans",sans-serif;color:var(--white)}
.quote-name b{font-weight:700}
.t-dots{left:548px;top:2457px;display:flex;gap:9px}
.t-dots span{width:14px;height:14px;border-radius:50%;border:2px solid #9aa3bf}
.t-dots span:nth-child(2){background:#b07a3c;border-color:#b07a3c}

/* footer */
.footer{left:0;top:2503px;width:1200px;height:283px;background:var(--footer)}
.footer-mark{left:150px;top:2568px;width:105px;height:105px;border-radius:50%;background:#9a6a34}
.foot-head{top:2558px;font:700 16px "Roboto",sans-serif;color:var(--white);letter-spacing:.5px}
.foot-list{top:2598px;list-style:none;font:12px/26px "Open Sans",sans-serif;color:var(--white)}
.news-input{left:799px;top:2597px;width:241px;height:35px;background:var(--white);font:11px/35px "Open Sans",sans-serif;color:#999;padding-left:14px;letter-spacing:.5px}
.news-btn{left:1040px;top:2597px;width:48px;height:35px;background:#1e8ad0;display:flex;align-items:center;justify-content:center}
.copyright{left:139px;top:2752px;font:9.5px "Open Sans",sans-serif;color:var(--white)}
.pay-label{left:687px;top:2754px;font:700 9px "Open Sans",sans-serif;color:var(--white)}
.pay-cards{left:845px;top:2740px;display:flex;gap:8px}
.pay-cards span{width:40px;height:28px;border-radius:4px;background:#e8ecf2}
</style>
</head>
<body>

<!-- header -->
<div class="abs brand"><span class="brand-mark"></span><span class="brand-name">Badgerline Custom Woodcraft</span></div>
<div class="abs call-label">CALL US TODAY!</div>
<div class="abs phone">
  <svg width="38" height="38" viewBox="0 0 24 24" aria-hidden="true"><path fill="#1b4f9c" d="M6.6 10.8a15.1 15.1 0 0 0 6.6 6.6l2.2-2.2a1 1 0 0 1 1-.25 11.4 11.4 0 0 0 3.6.57 1 1 0 0 1 1 1V20a1 1 0 0 1-1 1A17 17 0 0 1 3 4a1 1 0 0 1 1-1h3.5a1 1 0 0 1 1 1c0 1.25.2 2.45.57 3.57a1 1 0 0 1-.25 1z"/></svg>
  (555) 014-2738
</div>
<div class="abs hours">REACH US ON MON-SAT 8.00 - 17.00</div>

<!-- hero -->
<div class="abs hero" role="img" aria-label="Vertical wood plank background"></div>

<nav class="abs navbar">
  <div class="abs picker type">SELECT DESIGN TYPE <span>▾</span></div>
  <div class="abs picker qty">QTY <span>▾</span></div>
  <ul class="abs nav-links">
    <li style="width:90px">HOME</li>
    <li style="width:170px">OUR WOODWORKS</li>
    <li style="width:106px">PRICING</li>
    <li style="width:102px">REVIEWS</li>
    <li style="width:84px">HELP</li>
    <li style="width:130px">CONTACT US</li>
  </ul>
</nav>

<div class="abs disc" style="left:607px;top:142px;width:168px;height:168px;background:radial-gradient(#9c8c7e,#6a5a4c)" role="img" aria-label="Carved round wooden plaque with engraved emblem"></div>
<div class="abs disc" style="left:493px;top:266px;width:174px;height:174px;background:radial-gradient(#b5b0a8,#7b7672)" role="img" aria-label="Engraved metal disc with a farmhouse scene"></div>
<div class="abs disc" style="left:620px;top:390px;width:168px;height:168px;background:radial-gradient(#b86a4a,#8a4530)" role="img" aria-label="Carved red wood disc showing an eagle head"></div>

<div class="abs hero-banner"></div>
<h1 class="abs hero-title">Best of Custom Woodcraft?</h1>
<div class="abs hero-tag">BADGERLINE<br>HAS IT ALL!</div>
<div class="abs hero-cta">Request A Design Now!</div>
<div class="abs hero-dots"><span></span><span></span><span></span><span></span><span></span></div>

<form class="abs quote">
  <div class="abs quote-head">REQUEST A QUOTE</div>
  <div class="abs field" style="top:80px">Full Name <span>●</span></div>
  <div class="abs field" style="top:134px">Email <span>◉</span></div>
  <div class="abs field" style="top:186px">Phone <span>✆</span></div>
  <div class="abs field" style="top:236px">Select a Design <span>▾</span></div>
  <div class="abs submit">SUBMIT</div>
</form>

<section class="abs board welcome">
  <h2>Welcome To Badgerline</h2>
  <p>Lestie consequat, vel illum dolore eu feugiat nulla facilisis at vero eros et accumsan et iusto odio dignissim qui blandit praesent luptatum zzril delenit augue duis dolore te feugait nulla facilisi. Nam liber tempor cum soluta nobis eleifend option congue nihil imperdiet doming id quod mazim placerat facer possim assum.</p>
</section>
<div class="abs welcome-tip"></div>

<!-- designs -->
<h2 class="abs pill">Custom Designs From Badgerline</h2>

<h3 class="abs row-label" style="top:832px">Wood Plastic &amp; CNC</h3>
<div class="abs arrow-btn" style="left:54px;top:1009px"><svg width="30" height="30" viewBox="0 0 30 30"><path d="M18 8 L10 15 L18 22Z" fill="#c98a4e"/></svg></div>
<div class="abs arrow-btn" style="left:1112px;top:1009px"><svg width="30" height="30" viewBox="0 0 30 30"><path d="M12 8 L20 15 L12 22Z" fill="#c98a4e"/></svg></div>

<article class="abs card" style="left:111px;top:864px">
  <div class="card-photo" style="background:#a8563c" role="img" aria-label="Carved wooden eagle head"></div>
  <div class="card-title">Design Name/Type</div>
  <div class="card-desc">Short description here. liber tempor cum soluta nobis</div>
  <div class="card-rate"><span class="badge-new">New</span><span class="stars">★★★★★</span></div>
  <div class="card-btn">Get Pricing</div>
</article>
<article class="abs card" style="left:370px;top:864px">
  <div class="card-photo" style="background:#7a6b5c" role="img" aria-label="Carved round plaque with a building emblem"></div>
  <div class="card-title">Design Name/Type</div>
  <div class="card-desc">Short description here. liber tempor cum soluta nobis</div>
  <div class="card-rate"><span class="stars">★★★★★</span></div>
  <div class="card-btn">Get Pricing</div>
</article>
<article class="abs card" style="left:628px;top:864px">
  <div class="card-photo" style="background:#c7a47c" role="img" aria-label="Oval wooden tray with carved wildlife relief"></div>
  <div class="card-title">Design Name/Type</div>
  <div class="card-desc">Short description here. liber tempor cum soluta nobis</div>
  <div class="card-rate"><span class="badge-new">New</span><span class="stars">★★★★★</span></div>
  <div class="card-btn">Get Pricing</div>
</article>
<article class="abs card" style="left:888px;top:864px">
  <div class="card-photo" style="background:#b88a5a" role="img" aria-label="Pair of small wooden side tables"></div>
  <div class="card-title">Design Name/Type</div>
  <div class="card-desc">Short description here. liber tempor cum soluta nobis</div>
  <div class="card-rate"><span class="stars">★★★★★</span></div>
  <div class="card-btn">Get Pricing</div>
</article>

<h3 class="abs row-label" style="top:1261px">Metal Design</h3>
<div class="abs arrow-btn" style="left:54px;top:1439px"><svg width="30" height="30" viewBox="0 0 30 30"><path d="M18 8 L10 15 L18 22Z" fill="#c98a4e"/></svg></div>
<div class="abs arrow-btn" style="left:1112px;top:1425px"><svg width="30" height="30" viewBox="0 0 30 30"><path d="M12 8 L20 15 L12 22Z" fill="#c98a4e"/></svg></div>

<article class="abs card" style="left:111px;top:1294px">
  <div class="card-photo" style="background:#3e3c3a" role="img" aria-label="CNC machine engraving a metal emblem"></div>
  <div class="card-title">Design Name/Type</div>
  <div class="card-desc">Short description here. liber tempor cum soluta nobis</div>
  <div class="card-rate"><span class="badge-new">New</span><span class="stars">★★★★★</span></div>
  <div class="card-btn">Get Pricing</div>
</article>
<article class="abs card" style="left:370px;top:1294px">
  <div class="card-photo" style="background:#8d8984" role="img" aria-label="Engraved metal plate with a farm scene"></div>
  <div class="card-title">Design Name/Type</div>
  <div class="card-desc">Short description here. liber tempor cum soluta nobis</div>
  <div class="card-rate"><span class="stars">★★★★★</span></div>
  <div class="card-btn">Get Pricing</div>
</article>
<article class="abs card" style="left:628px;top:1294px">
  <div class="card-photo" style="background:#3e3c3a" role="img" aria-label="CNC machine engraving a metal emblem"></div>
  <div class="card-title">Design Name/Type</div>
  <div class="card-desc">Short description here. liber tempor cum soluta nobis</div>
  <div class="card-rate"><span class="stars">★★★★★</span></div>
  <div class="card-btn">Get Pricing</div>
</article>
<article class="abs card" style="left:888px;top:1294px">
  <div class="card-photo" style="background:#8d8984" role="img" aria-label="Engraved metal plate with a farm scene"></div>
  <div class="card-title">Design Name/Type</div>
  <div class="card-desc">Short description here. liber tempor cum soluta nobis</div>
  <div class="card-rate"><span class="badge-new">New</span><span class="stars">★★★★★</span></div>
  <div class="card-btn">Get Pricing</div>
</article>

<!-- recent projects -->
<h3 class="abs row-label" style="top:1699px">Recent WoodWorks Projects</h3>
<div class="tile" style="left:52px;top:1736px;width:303px;height:152px;background:#c49566" role="img" aria-label="Wooden nightstands in a workshop"></div>
<div class="tile" style="left:358px;top:1736px;width:303px;height:152px;background:#8b8782" role="img" aria-label="Engraved metal plate with a farm scene"></div>
<div class="tile" style="left:665px;top:1736px;width:301px;height:152px;background:#9a7a5a" role="img" aria-label="Wooden cabinet under a dartboard"></div>
<div class="tile" style="left:969px;top:1736px;width:179px;height:152px;background:#b89a7a" role="img" aria-label="Engraved wooden business sign"></div>
<div class="tile" style="left:52px;top:1892px;width:195px;height:154px;background:#7a5a3e" role="img" aria-label="Carved wood sculpture close-up"></div>
<div class="tile" style="left:251px;top:1892px;width:195px;height:154px;background:#6e5642" role="img" aria-label="Carved round wooden plaque"></div>
<div class="tile" style="left:449px;top:1892px;width:195px;height:154px;background:#444240" role="img" aria-label="CNC machine engraving metal"></div>
<div class="tile" style="left:648px;top:1892px;width:197px;height:154px;background:#a98c6c" role="img" aria-label="Engraved wooden sign"></div>
<div class="tile" style="left:849px;top:1892px;width:194px;height:154px;background:#a9553a" role="img" aria-label="Carved wooden eagle head"></div>
<div class="tile tile-more" style="left:1047px;top:1892px;width:101px;height:154px">View<br>All<br>Designs</div>

<!-- featured -->
<div class="abs navy-band"></div>
<section class="abs board feature">
  <h3>Featured In Timber Quarterly Magazine</h3>
  <p class="lede">Lorem ipsum dolor sit amet and some description here. Read More...</p>
  <p class="date">August 31, 2016, Pine Rd, Cedarvale, Alberta</p>
</section>
<div class="abs portrait-frame"><div style="width:100%;height:100%;background:linear-gradient(135deg,#8a6a4a,#4a3a2c)" role="img" aria-label="Portrait of the woodworker from the magazine interview"></div></div>
<div class="abs caption">Interview with Dale Morrow</div>

<p class="abs quote-text">“Badgerline WoodWorks was very excellent in dcrafting our liber tempor cum soluta nobis eleifend option congue nihil imperdiet doming id quod mazim placerat facer possim assum.</p>
<p class="abs quote-name"><b>Helen Carter,</b> 12 Birch Lane, Location, Alberta</p>
<div class="abs t-dots"><span></span><span></span><span></span><span></span><span></span></div>

<!-- footer -->
<footer class="abs footer"></footer>
<div class="abs footer-mark"></div>
<h4 class="abs foot-head" style="left:386px">QUICK LINKS</h4>
<ul class="abs foot-list" style="left:386px"><li>About Badgerline</li><li>Contact Us</li><li>Support</li><li>Reviews</li></ul>
<h4 class="abs foot-head" style="left:594px">CUSTOMERS</h4>
<ul class="abs foot-list" style="left:594px"><li>FAQ</li><li>Help</li><li>Pricing</li><li>Shipping &amp; Delivery</li></ul>
<h4 class="abs foot-head" style="left:799px">SIGN UP FOR OUR NEWS LETTER!</h4>
<div class="abs news-input">ENTER YOUR EMAIL ADDRESS</div>
<div class="abs news-btn"><svg width="20" height="16" viewBox="0 0 20 16"><path d="M2 8h14M10 2l6 6-6 6" stroke="#fff" stroke-width="2.5" fill="none"/></svg></div>
<p class="abs copyright">COPYRIGHT © 2016 - BADGERLINE. CUSTOM WOODCRAFT  ALL RIGHTS RESERVED.</p>
<p class="abs pay-label">AVAILABLE PAYMENT OPTIONS:</p>
<div class="abs pay-cards"><span></span><span></span><span></span><span></span><span></span></div>

</body>
</html>
```